Create awesome style / CSS for Quillgrid forms

The default Quillgrid form styles are kind of lame, but Quillgrid lets you add custom CSS that overrides the default to make them look like anything you want them to. I need you to create some awesome CSS to turn a bland looking form (ie: the default order form here: http://linkbrevo.example/7qm4tx2 ) into an amazing looking form.

THE STYLE OF THE FORM SHOULD BE CLEAN, CRISP AND CORPORATE.

You can either create an account with Quillgrid ( http://linkbrevo.example/7qm4wzk ) so you can experiment, or simply supply CSS code that I can test on my own forms.

```html
<!DOCTYPE html>
<html lang="en">
<head>
<meta charset="utf-8">
<title>Quillgrid Billing Form</title>
<link rel="stylesheet" href="https://fonts.googleapis.com/css2?family=Arimo:wght@400;700&display=swap">
<style>
  :root {
    --page: #ffffff;
    --panel: #e9e7e4;
    --panel-shadow: rgba(0,0,0,0.35);
    --brand: #2a9bcf;
    --brand-dark: #1f86b6;
    --text: #111111;
    --muted: #777777;
    --required: #cc0000;
    --field: #ffffff;
    --field-border: #c9c9c9;
    --arrow-bg: #f1f1f1;
  }
  * { box-sizing: border-box; margin: 0; padding: 0; }
  html, body { width: 1200px; height: 775px; overflow: hidden; background: var(--page); }
  body { position: relative; font-family: "Arimo", Arial, sans-serif; color: var(--text); }

  .form-panel {
    position: absolute; left: 288px; top: 16px; width: 624px; height: 744px;
    background: var(--panel); box-shadow: 0 1px 5px var(--panel-shadow);
  }
  .form-header {
    position: absolute; left: 9px; top: 8px; width: 606px; height: 72px;
    background: var(--brand); border-radius: 3px; color: #fff; text-align: center;
    box-shadow: 0 1px 2px rgba(0,0,0,0.25);
  }
  .form-title { font-size: 19px; font-weight: 700; margin-top: 13px; }
  .form-subtitle { font-size: 9.5px; margin-top: 9px; }

  .abs { position: absolute; }
  .label { font-size: 11px; font-weight: 700; }
  .label .req { color: var(--required); font-size: 15px; position: relative; top: -3px; margin-left: 1px; }
  .note { font-size: 12px; }
  .sublabel { font-size: 10px; font-weight: 700; color: var(--muted); }

  .field { background: var(--field); border: 1px solid var(--field-border); }
  .select { background: var(--field); border: 1px solid var(--field-border); }
  .select .arrow {
    position: absolute; right: 2px; top: 2px; bottom: 2px; width: 13px;
    background: var(--arrow-bg); border: 1px solid #b5b5b5; border-radius: 2px;
    display: flex; align-items: center; justify-content: center;
  }
  .total-box { font-size: 15px; font-weight: 700; padding: 9px 0 0 9px; }
  .currency { font-size: 15px; color: #444; }
  .submit {
    position: absolute; left: 249px; top: 688px; width: 126px; height: 36px;
    background: var(--brand); color: #fff; font-size: 15px; font-weight: 700;
    text-align: center; line-height: 36px; border-bottom: 2px solid var(--brand-dark);
  }
</style>
</head>
<body>
<main class="form-panel">
  <header class="form-header">
    <h1 class="form-title">Billing Information</h1>
    <p class="form-subtitle">Please fill out your billing information below.</p>
  </header>

  <div class="abs label" style="left:15px;top:98px">Card Number<span class="req">*</span></div>
  <div class="abs note" style="left:15px;top:114px">(Credit card fields have been disabled for this form.)</div>

  <div class="abs label" style="left:15px;top:139px">Card Expiration<span class="req">*</span></div>
  <div class="abs select" style="left:15px;top:155px;width:48px;height:20px"><span class="arrow"><svg width="7" height="5"><path d="M0 0h7L3.5 5z" fill="#444"/></svg></span></div>
  <div class="abs select" style="left:68px;top:155px;width:51px;height:20px"><span class="arrow"><svg width="7" height="5"><path d="M0 0h7L3.5 5z" fill="#444"/></svg></span></div>
  <svg class="abs" style="left:127px;top:153px" width="14" height="14" viewBox="0 0 14 14">
    <rect x="0.5" y="0.5" width="13" height="13" fill="#fff" stroke="#999"/>
    <rect x="0.5" y="0.5" width="13" height="3.5" fill="#d23a3a"/>
    <path d="M3 6v6M6 6v6M9 6v6M1 8h12M1 10.5h12" stroke="#aaa" stroke-width="0.8"/>
  </svg>

  <div class="abs label" style="left:15px;top:187px">Name<span class="req">*</span></div>
  <div class="abs field" style="left:15px;top:203px;width:292px;height:30px"></div>
  <div class="abs field" style="left:312px;top:203px;width:293px;height:30px"></div>
  <div class="abs sublabel" style="left:15px;top:236px">First Name</div>
  <div class="abs sublabel" style="left:312px;top:236px">Last Name</div>

  <div class="abs label" style="left:15px;top:262px">Address<span class="req">*</span></div>
  <div class="abs field" style="left:15px;top:277px;width:344px;height:31px"></div>
  <div class="abs field" style="left:15px;top:313px;width:344px;height:31px"></div>
  <div class="abs field" style="left:15px;top:349px;width:125px;height:32px"></div>
  <div class="abs select" style="left:145px;top:349px;width:147px;height:32px"><span class="arrow" style="top:8px;bottom:8px"><svg width="7" height="5"><path d="M0 0h7L3.5 5z" fill="#444"/></svg></span></div>
  <div class="abs field" style="left:300px;top:349px;width:71px;height:32px"></div>
  <div class="abs sublabel" style="left:15px;top:383px">City</div>
  <div class="abs sublabel" style="left:145px;top:383px">State</div>
  <div class="abs sublabel" style="left:300px;top:383px">Zip Code</div>

  <div class="abs label" style="left:15px;top:410px">Phone<span class="req">*</span></div>
  <div class="abs field" style="left:15px;top:424px;width:125px;height:31px"></div>

  <div class="abs label" style="left:15px;top:467px">Email<span class="req">*</span></div>
  <div class="abs field" style="left:15px;top:483px;width:344px;height:30px"></div>

  <div class="abs label" style="left:15px;top:524px">Quantity of Item 1 ($10 each)</div>
  <div class="abs select" style="left:15px;top:537px;width:30px;height:20px"><span class="arrow"><svg width="7" height="5"><path d="M0 0h7L3.5 5z" fill="#444"/></svg></span></div>

  <div class="abs label" style="left:15px;top:568px">Quantity of Item 2 ($10 each)</div>
  <div class="abs select" style="left:15px;top:581px;width:30px;height:20px"><span class="arrow"><svg width="7" height="5"><path d="M0 0h7L3.5 5z" fill="#444"/></svg></span></div>

  <div class="abs label" style="left:15px;top:613px">Total</div>
  <div class="abs currency" style="left:15px;top:632px">$</div>
  <div class="abs field total-box" style="left:27px;top:625px;width:62px;height:32px">0.00</div>

  <div class="submit">SUBMIT FORM</div>
</main>
</body>
</html>
```